New Business card design to reflect rebrand

I would like a business card design with a good base colour for our new logo and also a placeholder for a profile pic of the card holder. the design needs to be editable to the point that we can easily change the picture of the person and use that design for printlarkly etc. we are looking at a metalic finish business card so will need a good base colour to bring out the finish.

Target Market(s)

prospective customers

Industry/Entity Type

Business

Contact Information for Business Card

I would like one editable design that we can change the name of the card holder and profile picture. The design need to be in a format that be send to printlarkly etc.

Our address is Fenwick Lodge, Mill Lane, Ashcombe Vale, KT14 3WB Tel no. 01632 960418

Requirements
Must have
• place holder for a profile pic for the card holder. in AI or preferably PSD format

```html
<!DOCTYPE html>
<html lang="en">
<head>
<meta charset="utf-8">
<title>Orvane Workplace Services – Business Card</title>
<link rel="stylesheet" href="https://fonts.googleapis.com/css2?family=Roboto:wght@400;700&display=swap">
<style>
  :root {
    --page-bg: #ece9e4;
    --card-white: #ffffff;
    --card-navy: #1d3358;
    --accent-orange: #f26a21;
    --text-light: #e8ecf3;
    --logo-ink: #1d3358;
    --divider: rgba(255,255,255,0.22);
    --card-shadow: 0 18px 40px rgba(0,0,0,0.25);
  }
  * { box-sizing: border-box; margin: 0; padding: 0; }
  html, body {
    width: 1200px; height: 725px; overflow: hidden;
    background: var(--page-bg);
    font-family: "Roboto", Arial, sans-serif;
  }
  .card-set {
    position: relative; width: 1200px; height: 725px;
    display: flex; align-items: center; justify-content: center; gap: 50px;
  }
  .card {
    width: 540px; height: 320px; border-radius: 22px;
    box-shadow: var(--card-shadow); position: relative; overflow: hidden;
  }
  .card-front {
    background: linear-gradient(135deg, #ffffff 0%, #f1f1f1 100%);
    display: flex; align-items: center; justify-content: center;
  }
  .brand-name {
    color: var(--logo-ink); font-weight: 700; text-align: center;
    line-height: 1.1;
  }
  .brand-name .brand-main { display: block; font-size: 56px; letter-spacing: 3px; }
  .brand-name .brand-sub { display: block; font-size: 17px; letter-spacing: 5px; margin-top: 6px; }

  .card-back {
    background: var(--card-navy); color: var(--text-light);
    display: grid; grid-template-columns: 1fr 1px 1fr;
  }
  .holder {
    display: flex; flex-direction: column; align-items: center; justify-content: center;
    padding-bottom: 40px;
  }
  .holder-photo {
    width: 108px; height: 108px; border-radius: 50%;
    border: 4px solid #ffffff;
    background: radial-gradient(circle at 50% 40%, #c9a48f 0%, #6e4a3d 60%, #3a2a26 100%);
  }
  .holder-name {
    margin-top: 14px; color: var(--accent-orange);
    font-weight: 700; font-size: 17px; letter-spacing: 0.5px; text-transform: uppercase;
  }
  .holder-role { font-size: 12px; margin-top: 3px; color: var(--text-light); }
  .card-divider { background: var(--divider); margin: 40px 0; }
  .contact-list {
    list-style: none; display: flex; flex-direction: column; justify-content: center;
    gap: 14px; padding: 0 26px; font-size: 12.5px; line-height: 1.45;
  }
  .contact-item { display: flex; align-items: flex-start; gap: 12px; }
  .contact-icon { width: 14px; height: 14px; flex: 0 0 14px; margin-top: 1px; fill: var(--accent-orange); }
</style>
</head>
<body>
<main class="card-set">
  <section class="card card-front" aria-label="Card front">
    <h1 class="brand-name">
      <span class="brand-main">ORVANE</span>
      <span class="brand-sub">WORKPLACE SERVICES</span>
    </h1>
  </section>

  <section class="card card-back" aria-label="Card back">
    <div class="holder">
      <div class="holder-photo" role="img" aria-label="Profile photo of the card holder"></div>
      <p class="holder-name">Clara Benton</p>
      <p class="holder-role">Managing Partner</p>
    </div>
    <div class="card-divider"></div>
    <ul class="contact-list">
      <li class="contact-item">
        <svg class="contact-icon" viewBox="0 0 24 24" aria-hidden="true"><path d="M6.6 10.8a15 15 0 0 0 6.6 6.6l2.2-2.2a1 1 0 0 1 1-.25 11.4 11.4 0 0 0 3.6.57 1 1 0 0 1 1 1V20a1 1 0 0 1-1 1A17 17 0 0 1 3 4a1 1 0 0 1 1-1h3.5a1 1 0 0 1 1 1c0 1.25.2 2.45.57 3.57a1 1 0 0 1-.25 1z"/></svg>
        <span>01632 960418</span>
      </li>
      <li class="contact-item">
        <svg class="contact-icon" viewBox="0 0 24 24" aria-hidden="true"><path d="M12 2a7 7 0 0 0-7 7c0 5.25 7 13 7 13s7-7.75 7-13a7 7 0 0 0-7-7zm0 9.5A2.5 2.5 0 1 1 12 6.5a2.5 2.5 0 0 1 0 5z"/></svg>
        <span>Fenwick Lodge,<br>Mill Lane, Ashcombe Vale,<br>KT14 3WB</span>
      </li>
      <li class="contact-item">
        <svg class="contact-icon" viewBox="0 0 24 24" aria-hidden="true"><path d="M3 5h18a1 1 0 0 1 1 1v12a1 1 0 0 1-1 1H3a1 1 0 0 1-1-1V6a1 1 0 0 1 1-1zm9 7.5L4 7.3V8l8 5.2L20 8v-.7z"/></svg>
        <span>info@yoursite.com<br>www.yoursite.com</span>
      </li>
    </ul>
  </section>
</main>
</body>
</html>
```